Batch #27 - MEN'S NATURAL THERAPEUTIC INTIMATE WASH

Men's Natural Therapeutic INTIMATE Wash
BATCH #27

Design a 4 oz. stand up tube with flip top cap...
To be packaged in a carton/box

Formula contains Tea Tree OIL
Aloe Vera Gel
Coconut Oil

PRODUCT IS A WASH/SOAP

Helps with
- Jock Itch (tinea cruris)
- Skin Rashes
- Candida
- Itchy Skin

COLORS ON TUBE: Gray, Black, Lime Electric Green and Blue

PRODUCT FOR MEN!

Target Market(s)

MEN

Industry/Entity Type

Retail

Font styles to use
Sans Serif

Colors
9bcb3b
abd036
33a6d7
000000
c9c9c9

Requirements
Must have
• Colors... black, gray, electric green and blue
Nice to have
• Needs to look masculine appeal to the male consumer

```html
<!DOCTYPE html>
<html lang="en">
<head>
<meta charset="utf-8">
<title>Batch #27 – Men's Natural Therapeutic Intimate Wash</title>
<link rel="stylesheet" href="https://fonts.googleapis.com/css2?family=Questrial&family=Open+Sans:wght@400;600&display=swap">
<style>
  :root {
    --ink: #000000;
    --paper: #ffffff;
    --lime: #abd036;
    --blue: #33a6d7;
    --ghost: #1c1c1c;
    --gray: #c9c9c9;
  }
  * { margin: 0; padding: 0; box-sizing: border-box; }
  html, body { width: 817px; height: 1200px; overflow: hidden; background: var(--ink); }
  .label {
    position: relative;
    width: 817px;
    height: 1200px;
    background: var(--ink);
    overflow: hidden;
    font-family: "Open Sans", Arial, sans-serif;
    color: var(--paper);
  }
  .ghost-name {
    position: absolute;
    left: 10px;
    top: 1180px;
    transform-origin: 0 0;
    transform: rotate(-90deg);
    font-family: "Questrial", sans-serif;
    font-size: 215px;
    line-height: 1;
    color: var(--ghost);
    white-space: nowrap;
    letter-spacing: 4px;
  }
  .spine-line {
    position: absolute;
    left: 208px;
    top: 0;
    width: 4px;
    height: 990px;
    background: var(--paper);
  }
  .category-band {
    position: absolute;
    left: 0;
    top: 48px;
    width: 817px;
    height: 78px;
    background: var(--lime);
    display: flex;
    align-items: center;
    padding-left: 58px;
    color: var(--ink);
    font-weight: 600;
    font-size: 27px;
    white-space: nowrap;
  }
  .category-band .accent {
    font-family: "Questrial", sans-serif;
    font-weight: 400;
    font-size: 40px;
    margin: 0 8px;
  }
  .product-name {
    position: absolute;
    left: 250px;
    top: 150px;
    width: 440px;
    font-family: "Questrial", sans-serif;
    font-weight: 400;
    line-height: 1;
  }
  .product-name .word {
    display: block;
    font-size: 122px;
    letter-spacing: 6px;
  }
  .product-name .number {
    display: block;
    text-align: right;
    font-size: 122px;
    letter-spacing: 4px;
    margin-top: 12px;
  }
  .help-tag {
    position: absolute;
    left: 214px;
    top: 586px;
    width: 296px;
    height: 66px;
    background: var(--paper);
    color: var(--ink);
    display: flex;
    align-items: center;
    padding-left: 24px;
    font-size: 30px;
    font-weight: 600;
    letter-spacing: 2px;
  }
  .benefits {
    position: absolute;
    left: 236px;
    top: 680px;
    list-style: none;
    font-size: 28px;
    line-height: 37px;
  }
  .contains-tag {
    position: absolute;
    left: 0;
    top: 994px;
    width: 483px;
    height: 74px;
    background: var(--blue);
    color: var(--ink);
    display: flex;
    align-items: center;
    padding-left: 58px;
    font-size: 29px;
    font-weight: 600;
    letter-spacing: 3px;
  }
  .ingredients {
    position: absolute;
    left: 236px;
    top: 1088px;
    display: flex;
    gap: 26px;
    list-style: none;
    font-size: 24px;
    white-space: nowrap;
  }
  .ingredients li::before { content: "\2022"; margin-right: 2px; }
</style>
</head>
<body>
  <main class="label">
    <div class="ghost-name" aria-hidden="true">BATCH #27</div>
    <div class="spine-line"></div>

    <div class="category-band">Men's Natural Therapeutic <span class="accent">INTIMATE</span> Wash</div>

    <h1 class="product-name">
      <span class="word">BATCH</span>
      <span class="number">#27</span>
    </h1>

    <div class="help-tag">HELP WITH</div>
    <ul class="benefits">
      <li>Jock Itch (tinea cruris)</li>
      <li>Skin Rashes</li>
      <li>Candida</li>
      <li>Itchy Skin</li>
    </ul>

    <div class="contains-tag">FORMULA CONTAINS</div>
    <ul class="ingredients">
      <li>Coconut Oil</li>
      <li>Tea Tree OIL</li>
      <li>Aloe Vera Gel</li>
    </ul>
  </main>
</body>
</html>
```